Contact card for an aggressive entrepreneur

I am looking for a business/contact card as an individual. I operate under the company name The Varlow Circle, LLC (but don't generally use that other than for billing). I have explored a few ideas and am now turning to makerhive to connect with people more creative than me. I am trying to capture a diverse set of passions, which I will summarize with the following keywords (which may or may not be ON the card and are in no particular order):

entrepreneur
shark diver
MBA
visionary
defenseman
marketing guru
hockey coach
teacher
reader
writer
cook
captain
scuba diver
beach bum
Type A
Columbia
Vermont
New York
Montauk
founder
leader
focused
driven
teammate father

hope that makes some sense!
Updates

Please note the photo is for reference - unless there is a really creative way to use it I do not need a card with a head shot (I am not a model or an actor!)

Project Deadline Extended
Reason: There have been several requests to submit designs so we will close this project this Wednesday and select a design by this Friday. Thank you to all for your great ideas and submissions!

I am reviewing the designs and will select one by end of day tomorrow, Tuesday, EST
Thank you to all who participated!

Target Market(s)

everyone from business contacts to personal acquaintances

Industry/Entity Type

Business

Requirements
Must have
• Must be utterly original, extraordinary and memorable.
How it achieves that is up to you!
Essential contact information that needs to be included:

phone: (917) 555-4173
email: tomas@varlowcircle.example
skype: tomas.varlow
Nice to have
• A striking visual whether that is a photo or illustration
Some way of conveying the diversity of what I am and what I do
Feel free to use the printing or physical material of the card to make it stand out.
Should not have
• I am not into "logos" but that being said I do not want to limit creativity in any way so feel free to ignore any part of this brief if you disagree with me. No need to use the attached photo of me, but that's what I look like.

```html
<!DOCTYPE html>
<html lang="en">
<head>
<meta charset="utf-8">
<title>Tomas Varlow — Contact Card</title>
<link href="https://fonts.googleapis.com/css2?family=Montserrat:wght@300;400&display=swap" rel="stylesheet">
<style>
  :root {
    --backdrop: #bbbcbe;
    --card-paper: #f3f4f5;
    --card-paper-shade: #e4e6e8;
    --blue-deep: #0a6f99;
    --blue-mid: #1288ba;
    --blue-bright: #16a3dc;
    --blue-pale: #a9d7ec;
    --ghost-type: #d3e3ec;
    --white: #ffffff;
  }
  * { margin: 0; padding: 0; box-sizing: border-box; }
  html, body {
    width: 1200px;
    height: 901px;
    overflow: hidden;
    background: var(--backdrop);
    font-family: "Montserrat", "Helvetica Neue", Arial, sans-serif;
  }
  .card-set {
    position: relative;
    width: 1200px;
    height: 901px;
  }
  .card {
    position: absolute;
    top: 127px;
    width: 320px;
    height: 558px;
    overflow: hidden;
    background: linear-gradient(160deg, var(--white) 0%, var(--card-paper) 55%, var(--card-paper-shade) 100%);
  }
  .card--front { left: 209px; }
  .card--back { left: 661px; }
  .card svg { display: block; width: 100%; height: 100%; }
  .card__name {
    font-family: "Montserrat", "Helvetica Neue", Arial, sans-serif;
    font-weight: 300;
    font-size: 25px;
    letter-spacing: 4px;
    fill: var(--blue-mid);
  }
  .ghost-name {
    font-family: "Montserrat", "Helvetica Neue", Arial, sans-serif;
    font-weight: 300;
    fill: var(--ghost-type);
  }
  .contact-line {
    font-family: "Montserrat", "Helvetica Neue", Arial, sans-serif;
    font-weight: 400;
    font-size: 15px;
    letter-spacing: 2px;
    fill: var(--white);
  }
</style>
</head>
<body>
<main class="card-set">

  <section class="card card--front" aria-label="Card front">
    <svg viewBox="0 0 320 558" xmlns="http://www.w3.org/2000/svg">
      <defs>
        <linearGradient id="stripe-fade" x1="0" y1="1" x2="1" y2="0">
          <stop offset="0" stop-color="var(--blue-deep)"/>
          <stop offset="0.55" stop-color="var(--blue-bright)" stop-opacity="0.7"/>
          <stop offset="1" stop-color="var(--blue-pale)" stop-opacity="0"/>
        </linearGradient>
        <linearGradient id="stripe-soft" x1="0" y1="1" x2="1" y2="0">
          <stop offset="0" stop-color="var(--blue-mid)" stop-opacity="0.8"/>
          <stop offset="1" stop-color="var(--blue-pale)" stop-opacity="0"/>
        </linearGradient>
        <linearGradient id="fold-shade" x1="0" y1="0" x2="0" y2="1">
          <stop offset="0" stop-color="#d9dcdf"/>
          <stop offset="1" stop-color="var(--card-paper)"/>
        </linearGradient>
      </defs>

      <g class="stripes">
        <polygon points="0,150 150,0 250,0 0,250" fill="url(#stripe-soft)" opacity="0.55"/>
        <polygon points="0,185 185,0 200,0 0,200" fill="url(#stripe-fade)"/>
        <polygon points="0,232 232,0 242,0 0,242" fill="var(--white)" opacity="0.8"/>
        <polygon points="0,258 258,0 282,0 0,282" fill="url(#stripe-fade)"/>
        <polygon points="0,300 230,70 250,70 0,320" fill="url(#stripe-soft)"/>
        <polygon points="0,345 240,105 250,105 0,355" fill="url(#stripe-fade)"/>
        <polygon points="0,380 235,145 240,150 0,395" fill="url(#stripe-fade)" opacity="0.8"/>
        <polygon points="0,410 260,150 275,150 0,440" fill="var(--blue-deep)"/>
      </g>

      <g class="fold">
        <polygon points="0,500 209,303 320,403 320,558 0,558" fill="url(#fold-shade)"/>
        <polygon points="209,303 320,200 320,403" fill="var(--white)" opacity="0.7"/>
      </g>

      <text class="card__name" x="160" y="522" text-anchor="middle">TOMAS VARLOW</text>
    </svg>
  </section>

  <section class="card card--back" aria-label="Card back">
    <svg viewBox="0 0 320 558" xmlns="http://www.w3.org/2000/svg">
      <defs>
        <linearGradient id="band-blue" x1="0" y1="1" x2="1" y2="0">
          <stop offset="0" stop-color="var(--blue-deep)"/>
          <stop offset="0.5" stop-color="var(--blue-bright)"/>
          <stop offset="1" stop-color="var(--blue-deep)"/>
        </linearGradient>
      </defs>

      <g class="ghost-names">
        <text class="ghost-name" x="-40" y="68" font-size="44" letter-spacing="4">TOMAS VARLOW</text>
        <text class="ghost-name" x="-20" y="165" font-size="28" letter-spacing="4">TOMAS VARLOW</text>
        <text class="ghost-name" x="210" y="328" font-size="44" letter-spacing="4">TOMAS</text>
        <text class="ghost-name" x="-30" y="445" font-size="48" letter-spacing="4">TOMAS VARLOW</text>
        <text class="ghost-name" x="92" y="532" font-size="24" letter-spacing="4">TOMAS VARLOW</text>
      </g>

      <polygon class="contact-band" points="0,340 320,23 320,200 0,517" fill="url(#band-blue)"/>
      <polygon points="120,400 320,200 320,140 200,260" fill="var(--blue-bright)" opacity="0.35"/>

      <g class="contact-details" transform="translate(18,420) rotate(-44.7)">
        <text class="contact-line" x="0" y="-22">phone: (917) 555-4173</text>
        <text class="contact-line" x="0" y="0">email: tomas@varlowcircle.example</text>
        <text class="contact-line" x="0" y="22">skype: tomas.varlow</text>
      </g>
    </svg>
  </section>

</main>
</body>
</html>
```